Business card for exciting VC company

Should look simple, crisp, and modern.

Industry/Entity Type

Venture Capital

Contact Information for Business Card

Would like to see at least one design that has our blue on the back with the tagline "Transforming Traditional Industry" and white front with contact details.

Font styles to use
Sans Serif

Requirements
Must have
• Logo

Gregory Tallis
gtallis@brindlewave.vc
Managing Partner
M (628)354-xxxx

```html
<!DOCTYPE html>
<html lang="en">
<head>
<meta charset="utf-8">
<title>Brindlewave Capital – Business Card</title>
<link rel="stylesheet" href="https://fonts.googleapis.com/css2?family=Montserrat:wght@500;600&family=Open+Sans:wght@400;600&display=swap">
<style>
  :root {
    --brand-blue: #4182c6;
    --ink-black: #000000;
    --paper-white: #ffffff;
    --rule-grey: #c8c8c8;
    --stage: #2a2a2a;
  }
  * { margin: 0; padding: 0; box-sizing: border-box; }
  html, body { width: 1200px; height: 1015px; overflow: hidden; }
  body {
    background: var(--stage);
    display: flex;
    flex-direction: column;
    align-items: center;
    justify-content: center;
    gap: 56px;
    font-family: "Open Sans", Arial, sans-serif;
  }
  .card {
    position: relative;
    width: 700px;
    height: 400px;
    overflow: hidden;
    box-shadow: 0 10px 30px rgba(0,0,0,.45);
  }

  /* Back of card */
  .card-back { background: var(--ink-black); }
  .card-back .wordmark {
    position: absolute;
    top: 0; left: 0; right: 0;
    height: 292px;
    display: flex;
    align-items: center;
    justify-content: center;
    color: var(--paper-white);
    font-size: 40px;
  }
  .band {
    position: absolute;
    left: 0; right: 0; bottom: 0;
    background: var(--brand-blue);
    display: flex;
    align-items: center;
    justify-content: center;
    color: var(--paper-white);
  }
  .card-back .band { height: 108px; }
  .tagline {
    font-family: "Montserrat", Arial, sans-serif;
    font-weight: 500;
    font-size: 17px;
    letter-spacing: 1.5px;
    text-transform: uppercase;
  }

  /* Front of card */
  .card-front { background: var(--paper-white); }
  .card-front .band { height: 124px; }
  .website { font-size: 22px; letter-spacing: .5px; }
  .wordmark {
    font-family: "Montserrat", Arial, sans-serif;
    font-weight: 500;
    letter-spacing: 3px;
    text-transform: uppercase;
    white-space: nowrap;
  }
  .card-front .wordmark {
    position: absolute;
    left: 0;
    width: 346px;
    top: 0;
    height: 276px;
    display: flex;
    align-items: center;
    justify-content: center;
    color: var(--ink-black);
    font-size: 22px;
  }
  .divider {
    position: absolute;
    left: 346px;
    top: 70px;
    width: 1px;
    height: 138px;
    background: var(--rule-grey);
  }
  .contact {
    position: absolute;
    left: 380px;
    top: 78px;
    color: var(--ink-black);
  }
  .contact-name {
    color: var(--brand-blue);
    font-weight: 600;
    font-size: 25px;
    text-transform: uppercase;
    letter-spacing: -.3px;
    line-height: 1;
  }
  .contact-title { font-size: 19px; margin-top: 2px; }
  .contact-lines { list-style: none; margin-top: 14px; }
  .contact-lines li {
    display: flex;
    align-items: center;
    gap: 10px;
    font-size: 19px;
    line-height: 1.35;
  }
  .contact-lines svg { width: 18px; height: 18px; flex: none; }
</style>
</head>
<body>

  <section class="card card-back" aria-label="Business card, back">
    <div class="wordmark">Brindlewave Capital</div>
    <div class="band">
      <p class="tagline">Transforming Traditional Industry</p>
    </div>
  </section>

  <section class="card card-front" aria-label="Business card, front">
    <div class="wordmark">Brindlewave Capital</div>
    <span class="divider"></span>
    <div class="contact">
      <p class="contact-name">Gregory Tallis</p>
      <p class="contact-title">Managing Partner</p>
      <ul class="contact-lines">
        <li>
          <svg viewBox="0 0 24 24" aria-hidden="true">
            <path fill="#4182c6" d="M6.6 10.8a15.1 15.1 0 0 0 6.6 6.6l2.2-2.2a1 1 0 0 1 1-.25 11.4 11.4 0 0 0 3.6.57 1 1 0 0 1 1 1V20a1 1 0 0 1-1 1A17 17 0 0 1 3 4a1 1 0 0 1 1-1h3.5a1 1 0 0 1 1 1c0 1.25.2 2.45.57 3.57a1 1 0 0 1-.25 1z"/>
          </svg>
          (628)354-xxxx
        </li>
        <li>
          <svg viewBox="0 0 24 24" aria-hidden="true">
            <rect x="2" y="5" width="20" height="14" fill="#4182c6"/>
            <path d="M2 5l10 8 10-8" fill="none" stroke="#ffffff" stroke-width="1.6"/>
          </svg>
          gtallis@brindlewave.vc
        </li>
      </ul>
    </div>
    <div class="band">
      <p class="website">www.brindlewave.vc</p>
    </div>
  </section>

</body>
</html>
```